Whitmore Business Card Design

The name of the business is Dara Whitmore, CPA LLC
The service that we offer is Accounting, Tax & Consulting Services. I need it to have the following items:
Dara Whitmore, Principal
Phone Number
Email Address
Physical Address

I have attached the company logo, one in black and one in white. Please provide a design in black background and the other in white background. Please include "Accounting, Tax & Consulting Services". I want the business card to be clean and very professional.

```html
<!DOCTYPE html>
<html lang="en">
<head>
<meta charset="utf-8">
<title>Dara Whitmore, CPA LLC – Business Card</title>
<link href="https://fonts.googleapis.com/css2?family=Montserrat:wght@400;500;600&display=swap" rel="stylesheet">
<style>
  :root {
    --backdrop: #d3d3d3;
    --card: #ffffff;
    --card-dark: #1e1e20;
    --brand-red: #9b1b1e;
    --ink-dark: #3a3a3c;
    --ink-grey: #8a8a8a;
    --ink-light: #f2f2f2;
    --ink-soft: #b4b4b4;
    --rule: #a9a9a9;
  }
  html, body {
    margin: 0;
    padding: 0;
    width: 1000px;
    height: 1200px;
    overflow: hidden;
    background: var(--backdrop);
    font-family: "Montserrat", sans-serif;
  }
  .canvas { position: relative; width: 1000px; height: 1200px; }
  .card {
    position: absolute;
    left: 134px;
    width: 732px;
    height: 419px;
    background: var(--card);
    box-shadow: 2px 3px 5px rgba(0,0,0,0.28);
  }
  .card--front { top: 159px; }
  .card--back { top: 622px; background: var(--card-dark); }

  .brand-mark { position: absolute; background: var(--ink-dark); }
  .brand-name {
    position: absolute;
    margin: 0;
    color: var(--ink-dark);
    font-weight: 600;
    white-space: nowrap;
  }
  .brand-tagline {
    position: absolute;
    margin: 0;
    color: var(--ink-grey);
    font-weight: 500;
    white-space: nowrap;
  }

  /* front */
  .card--front .brand-mark { left: 65px; top: 50px; width: 74px; height: 74px; }
  .card--front .brand-name { left: 167px; top: 52px; font-size: 31px; letter-spacing: 2.6px; }
  .card--front .brand-tagline { left: 167px; top: 94px; font-size: 22px; letter-spacing: 4.6px; }

  .person-name {
    position: absolute; left: 64px; top: 204px; margin: 0;
    color: var(--brand-red); font-size: 25px; font-weight: 600;
  }
  .person-title {
    position: absolute; left: 64px; top: 238px; margin: 0;
    color: var(--ink-grey); font-size: 18px; font-weight: 400;
  }
  .divider {
    position: absolute; left: 64px; top: 280px; width: 603px;
    height: 0; border-top: 1.5px solid var(--rule);
  }
  .contact-list {
    position: absolute; left: 64px; top: 302px; margin: 0; padding: 0;
    list-style: none; color: var(--ink-grey); font-size: 17.5px; line-height: 24.5px;
  }
  .contact-list li { display: flex; align-items: center; }
  .contact-list svg { width: 16px; height: 16px; margin-right: 13px; fill: var(--brand-red); }
  .address {
    position: absolute; right: 65px; top: 302px; margin: 0;
    text-align: right; font-style: normal;
    color: var(--ink-grey); font-size: 17.5px; line-height: 24.5px;
  }

  /* back – dark version */
  .card--back .brand-mark { left: 313px; top: 108px; width: 106px; height: 106px; background: var(--ink-light); }
  .card--back .brand-name {
    left: 0; width: 732px; text-align: center; top: 230px;
    font-size: 30px; letter-spacing: 1.8px; color: var(--ink-light);
  }
  .card--back .brand-tagline {
    left: 0; width: 732px; text-align: center; top: 268px;
    font-size: 21px; letter-spacing: 3.6px; color: var(--ink-soft);
  }
  .services {
    position: absolute; left: 0; width: 732px; top: 308px; margin: 0;
    text-align: center; color: var(--ink-soft);
    font-size: 15px; font-weight: 400; letter-spacing: 1.5px;
  }
</style>
</head>
<body>
<div class="canvas">

  <section class="card card--front" aria-label="Business card front">
    <div class="brand-mark"></div>
    <p class="brand-name">DARA WHITMORE, CPA LLC</p>
    <p class="brand-tagline">CERTIFIED PUBLIC ACCOUNTANT</p>

    <h1 class="person-name">Dara Whitmore</h1>
    <p class="person-title">Principal</p>
    <div class="divider"></div>

    <ul class="contact-list">
      <li>
        <svg viewBox="0 0 16 16" aria-hidden="true"><path d="M3.2 1.5l2.3 2.6-1.2 1.6c.9 2.3 2.5 4 4.8 5l1.6-1.2 2.6 2.3-1.4 2c-5.8-.6-10-4.8-10.5-10.7z"/></svg>
        1-800-555-0148
      </li>
      <li>
        <svg viewBox="0 0 16 16" aria-hidden="true"><path d="M1 4h14v1.2L8 9.3 1 5.2z M1 6.8l7 4 7-4V12H1z"/></svg>
        info@website.com
      </li>
      <li>
        <svg viewBox="0 0 16 16" aria-hidden="true"><path d="M8 1.5a6.5 6.5 0 1 0 0 13 6.5 6.5 0 0 0 0-13zm-.7 1.6v2.4H5.1c.5-1.3 1.3-2.2 2.2-2.4zm1.4 0c.9.2 1.7 1.1 2.2 2.4H8.7zM4.6 6.9h2.7v2.2H4.6a7 7 0 0 1 0-2.2zm4.1 0h2.7a7 7 0 0 1 0 2.2H8.7zM3.2 6.9a5 5 0 0 0 0 2.2H2.9a5.2 5.2 0 0 1 0-2.2zm9.6 0h.3a5.2 5.2 0 0 1 0 2.2h-.3a5 5 0 0 0 0-2.2zM5.1 10.5h2.2v2.4c-.9-.2-1.7-1.1-2.2-2.4zm3.6 0h2.2c-.5 1.3-1.3 2.2-2.2 2.4z"/></svg>
        www.website.com
      </li>
    </ul>

    <address class="address">
      2470 Alder Ridge Rd<br>
      Maple Hollow<br>
      Minnesota(MN)
    </address>
  </section>

  <section class="card card--back" aria-label="Business card back, dark version">
    <div class="brand-mark"></div>
    <p class="brand-name">DARA WHITMORE, CPA LLC</p>
    <p class="brand-tagline">CERTIFIED PUBLIC ACCOUNTANT</p>
    <p class="services">Accounting, Tax &amp; Consulting Services</p>
  </section>

</div>
</body>
</html>
```